13 Tavo - new website design project

Our company Tavo Electrical is developing a new lead generation website focused on Electrical, LED Lighting and Solar Power. We need a high converting website.

Example of our current website is www.tavoelectrical.com.au You can take content from this website for this new design. Our colours are red, black and white. For our new website we would like to promote Tavo, Bright Days Ahead. Please listen to the jingle.

The below link is the company jingle that we have developed.
http://www.tunecraftaudio.com.au/tav-tc-v1/

The key for this brief is to generate leads for Electrical, LED Lighting (for commercial) and Solar Power & Storage.

Target Market(s)

Business owners in Melbourne Victoria

Number of Pages Required

4 page

Colors
ec1f27
ffffff

Requirements
Must have
• This page must be clean, be in line with company branding and a high converting lead website.

```html
<!DOCTYPE html>
<html lang="en">
<head>
<meta charset="utf-8">
<title>Tavo Electrical</title>
<link rel="stylesheet" href="https://fonts.googleapis.com/css2?family=Jost:wght@400;500&family=Open+Sans:wght@400;600;700&display=swap">
<style>
:root{
  --red:#ec1f27;
  --red-soft:rgba(236,31,39,.85);
  --ink:#333;
  --grey-text:#777;
  --light:#ececec;
  --white:#fff;
  --footer:#333537;
  --footer-line:#555;
  --social-square:#5c6f86;
}
*{margin:0;padding:0;box-sizing:border-box}
html,body{width:1200px;height:2647px;overflow:hidden;background:var(--white)}
body{position:relative;font-family:"Jost",sans-serif;color:var(--ink)}
.abs{position:absolute}
/* header */
.brand{left:132px;top:30px;display:flex;align-items:center;gap:10px;font:500 34px "Jost",sans-serif;color:var(--red)}
.brand-dot{width:18px;height:18px;border-radius:50%;background:var(--red)}
.contact-bar{top:22px;right:132px;display:flex;gap:36px;font:400 13px "Jost",sans-serif;color:var(--ink)}
.contact-item{display:flex;align-items:center;gap:12px}
.ring{width:24px;height:24px;border:1.5px solid var(--red);border-radius:50%;display:flex;align-items:center;justify-content:center}
.nav{top:76px;right:132px;display:flex;gap:62px;font:400 12px "Jost",sans-serif;text-transform:uppercase}
.nav a{color:var(--ink);text-decoration:none;position:relative;padding-bottom:15px}
.nav a.active{color:var(--red)}
.nav a.active::after{content:"";position:absolute;left:-6px;right:-6px;bottom:0;height:3px;background:var(--red)}
/* hero */
.hero{left:0;top:110px;width:1200px;height:458px;background:linear-gradient(180deg,#d9dadc 0%,#c4c4c6 45%,#a9a6a4 80%,#8a7d74 100%)}
.hero-caption{left:0;top:355px;width:556px;height:150px;background:rgba(70,70,70,.72);padding:24px 0 0 130px;color:var(--white)}
.hero-caption .kicker{font:400 26px "Open Sans",sans-serif;letter-spacing:.5px}
.hero-caption h1{font:700 56px "Open Sans",sans-serif;line-height:1.15;margin-top:6px}
.dots{top:528px;left:576px;display:flex;gap:8px}
.dots span{width:10px;height:10px;border-radius:50%;background:#ddd}
.dots span.on{background:var(--red)}
/* welcome */
.welcome{left:0;top:568px;width:1200px;height:593px;background:var(--light)}
.welcome-photo{left:132px;top:657px;width:394px;height:423px;background:linear-gradient(160deg,#e8dccb 0%,#b89c7c 50%,#6d5442 100%)}
.welcome-card{left:388px;top:683px;width:680px;height:362px;background:var(--white);padding:68px 30px 0 27px}
.welcome-card h2{font:400 31px "Jost",sans-serif;color:var(--red);margin-left:8px}
.welcome-card p{font:400 11.5px/2.2 "Jost",sans-serif;color:var(--grey-text);margin-top:22px}
.btn{display:inline-block;margin-top:42px;width:124px;height:41px;background:var(--red);color:var(--white);font:400 11px/41px "Jost",sans-serif;text-align:center;border-radius:3px;text-transform:uppercase}
/* section titles */
.section-title{left:0;width:1200px;text-align:center;font:400 31px "Jost",sans-serif;color:var(--red);text-transform:uppercase}
/* services */
.service{top:1297px;width:300px;height:224px}
.service .ph{width:100%;height:100%}
.service .band{position:absolute;left:0;bottom:0;width:100%;height:60px;background:var(--red-soft);color:var(--white);font:400 20px/60px "Jost",sans-serif;padding-left:21px;text-transform:uppercase}
/* testimonials */
.testimonials{left:0;top:1615px;width:1200px;height:344px;background:linear-gradient(180deg,#f3f4f5,#eceeef)}
.avatar{left:138px;top:1761px;width:106px;height:106px;border-radius:50%;border:4px solid var(--white);box-shadow:0 0 0 1px #ccc;background:linear-gradient(180deg,#8a7a66,#4b4036)}
.quote{left:282px;top:1769px;width:820px;font:400 12px/2.1 "Jost",sans-serif;color:#8a8a8a}
.quote .name{color:var(--red);font-size:11px;margin-top:12px}
.quote .role{color:var(--ink);font-size:11px;line-height:1.6}
.arrow{top:1791px;width:22px;height:22px;border:1px solid #555;border-radius:50%;display:flex;align-items:center;justify-content:center}
/* why */
.why{top:2115px;width:220px;text-align:center;font:400 19px/1.25 "Jost",sans-serif;color:var(--red);text-transform:uppercase}
.why svg{display:block;margin:0 auto 12px;height:42px}
/* footer */
.footer{left:0;top:2286px;width:1200px;height:361px;background:linear-gradient(160deg,#3a3c3e,#2c2d2f)}
.f-head{top:2356px;font:400 19px "Jost",sans-serif;color:var(--white);text-transform:uppercase}
.f-list{top:2404px;list-style:none;font:400 12px "Open Sans",sans-serif;color:var(--white)}
.f-list li{height:24px;display:flex;align-items:center;gap:10px}
.sq{width:18px;height:18px;background:var(--social-square);flex:none}
.f-field{left:884px;width:184px;height:24px;border-bottom:1px solid #777;font:400 11px "Open Sans",sans-serif;color:#aaa}
.f-submit{left:884px;top:2489px;width:78px;height:30px;border:1px solid #aaa;border-radius:3px;color:#ddd;font:400 11px/28px "Open Sans",sans-serif;text-align:center}
.f-rule{left:132px;top:2577px;width:936px;height:1px;background:var(--footer-line)}
.copy{left:0;top:2602px;width:1200px;text-align:center;font:400 11px "Open Sans",sans-serif;color:var(--white)}
</style>
</head>
<body>

<header>
  <div class="abs brand"><span class="brand-dot"></span>Tavo</div>
  <div class="abs contact-bar">
    <div class="contact-item"><span class="ring"><svg width="12" height="12" viewBox="0 0 24 24"><path fill="#ec1f27" d="M6.6 10.8a15 15 0 0 0 6.6 6.6l2.2-2.2c.3-.3.7-.4 1-.2 1.1.4 2.3.6 3.6.6.6 0 1 .4 1 1V20c0 .6-.4 1-1 1A17 17 0 0 1 3 4c0-.6.4-1 1-1h3.5c.6 0 1 .4 1 1 0 1.3.2 2.5.6 3.6.1.3 0 .7-.2 1z"/></svg></span>(571) 555-0142</div>
    <div class="contact-item"><span class="ring"><svg width="12" height="10" viewBox="0 0 24 18"><rect x="1" y="1" width="22" height="16" fill="none" stroke="#ec1f27" stroke-width="2"/><path d="M1 1l11 9 11-9" fill="none" stroke="#ec1f27" stroke-width="2"/></svg></span>info@tavomail.com</div>
  </div>
  <nav class="abs nav">
    <a class="active" href="#">Home</a><a href="#">Tavo Story</a><a href="#">Services</a><a href="#">Our Work</a><a href="#">Contact Us</a>
  </nav>
</header>

<section class="abs hero" role="img" aria-label="Bright white living room with pendant chandelier, grey sofa and shuttered windows"></section>
<div class="abs hero-caption">
  <div class="kicker">RESIDENTIAL &amp; COMMERCIAL</div>
  <h1>LED LIGHTING</h1>
</div>
<div class="abs dots"><span></span><span class="on"></span><span></span></div>

<section class="abs welcome"></section>
<div class="abs welcome-photo" role="img" aria-label="Warm lit lounge with a sculpted pendant lamp and cushions"></div>
<div class="abs welcome-card">
  <h2>WELCOME TO TAVO ELECTRICAL</h2>
  <p>Tavo Electrical was formed to be an expert Electricity Contracting Company providing services to all Residential and Commercial Customers. With over 10 years of experience, Tavo Electrical has developed a highly-experienced team of professionals that ensure all our customer expectations are met.</p>
  <a class="btn">Read More</a>
</div>

<h2 class="abs section-title" style="top:1208px">Our Services</h2>
<div class="abs service" style="left:132px"><div class="ph" role="img" aria-label="Electricians in hard hats working at a switchboard" style="background:linear-gradient(135deg,#d8d4c8,#8d8676 60%,#5a544b)"></div><div class="band">Electrical</div></div>
<div class="abs service" style="left:450px"><div class="ph" role="img" aria-label="Close-up of LED light bulbs" style="background:linear-gradient(135deg,#f2f2f2,#bfc2c6 55%,#8d9096)"></div><div class="band">LED Lighting</div></div>
<div class="abs service" style="left:768px"><div class="ph" role="img" aria-label="Worker in a hard hat beside solar panels under blue sky" style="background:linear-gradient(160deg,#cfe6fb,#5b9fe0 55%,#2f62b0)"></div><div class="band">Solar Power</div></div>

<section class="abs testimonials"></section>
<h2 class="abs section-title" style="top:1671px">Testimonials</h2>
<div class="abs arrow" style="left:93px"><svg width="8" height="10" viewBox="0 0 8 10"><path d="M6 1L2 5l4 4" fill="none" stroke="#555" stroke-width="1.5"/></svg></div>
<div class="abs arrow" style="left:1096px"><svg width="8" height="10" viewBox="0 0 8 10"><path d="M2 1l4 4-4 4" fill="none" stroke="#555" stroke-width="1.5"/></svg></div>
<div class="abs avatar" role="img" aria-label="Warehouse interior thumbnail"></div>
<div class="abs quote">
  <p>The service, communication and after sales service of Tavo Electrical has been awesome. We would strongly recommend them to any business contemplating upgrading their lighting or any other electrical work.</p>
  <p class="name">Dean Holloway</p>
  <p class="role">General Manager Boardline</p>
</div>

<h2 class="abs section-title" style="top:2022px">Why Choose Us?</h2>
<div class="abs why" style="left:91px"><svg viewBox="0 0 30 42" width="30"><path d="M15 3a11 11 0 0 0-6 20v6h12v-6a11 11 0 0 0-6-20z" fill="none" stroke="#777" stroke-width="3"/><rect x="10" y="32" width="10" height="3" fill="#777"/><rect x="11" y="37" width="8" height="3" fill="#777"/></svg>Professional<br>Service</div>
<div class="abs why" style="left:303px"><svg viewBox="0 0 30 42" width="30"><path d="M8 18v-6a7 7 0 0 1 14 0v6" fill="none" stroke="#777" stroke-width="4"/><rect x="3" y="18" width="24" height="21" rx="2" fill="#777"/></svg>5 Year Workmanship<br>Guarantee</div>
<div class="abs why" style="left:515px"><svg viewBox="0 0 50 42" width="50"><rect x="2" y="9" width="46" height="26" fill="#777"/><rect x="7" y="14" width="36" height="16" fill="#fff"/><circle cx="25" cy="22" r="6" fill="#777"/></svg>Value for<br>Money</div>
<div class="abs why" style="left:712px"><svg viewBox="0 0 46 42" width="46"><path d="M4 38C6 18 20 6 42 6c0 20-12 30-30 28z" fill="#777"/><path d="M4 38L30 16" stroke="#fff" stroke-width="2"/></svg>Environmentally<br>Friendly</div>
<div class="abs why" style="left:919px"><svg viewBox="0 0 44 42" width="44"><rect x="2" y="18" width="9" height="22" fill="#777"/><path d="M14 20l8-16c4 0 5 3 4 8h12c3 0 4 3 3 5l-4 19c-1 3-3 4-5 4H14z" fill="#777"/></svg>Fully<br>Insured</div>

<footer class="abs footer" role="img" aria-label="Dark blurred office interior backdrop"></footer>
<h3 class="abs f-head" style="left:132px">Quick Links</h3>
<ul class="abs f-list" style="left:132px"><li>Home</li><li>Tavo Story</li><li>Service</li><li>Our Work</li><li>Contact Us</li></ul>
<h3 class="abs f-head" style="left:381px">Social Media</h3>
<ul class="abs f-list" style="left:381px"><li><span class="sq"></span>Pulsefeed</li><li><span class="sq"></span>Friendhub</li><li><span class="sq"></span>Workweb</li><li><span class="sq"></span>Clipcast</li></ul>
<h3 class="abs f-head" style="left:628px">Address</h3>
<ul class="abs f-list" style="left:632px;font-size:11px">
  <li><svg width="12" height="12" viewBox="0 0 24 24"><path fill="#fff" d="M6.6 10.8a15 15 0 0 0 6.6 6.6l2.2-2.2c.3-.3.7-.4 1-.2 1.1.4 2.3.6 3.6.6.6 0 1 .4 1 1V20c0 .6-.4 1-1 1A17 17 0 0 1 3 4c0-.6.4-1 1-1h3.5c.6 0 1 .4 1 1 0 1.3.2 2.5.6 3.6.1.3 0 .7-.2 1z"/></svg>714-555-0188</li>
  <li><svg width="12" height="12" viewBox="0 0 24 24"><rect x="6" y="2" width="12" height="6" fill="#fff"/><rect x="2" y="9" width="20" height="9" fill="#fff"/><rect x="6" y="15" width="12" height="7" fill="#fff"/></svg>714-555-0193</li>
  <li><svg width="12" height="10" viewBox="0 0 24 18"><rect x="1" y="1" width="22" height="16" fill="#fff"/><path d="M1 1l11 9 11-9" fill="none" stroke="#333" stroke-width="2"/></svg><span style="text-decoration:underline">service@tavoelectrical.com.au</span></li>
  <li style="height:auto;align-items:flex-start;padding-top:5px"><svg width="12" height="14" viewBox="0 0 24 30"><path fill="#fff" d="M12 0a10 10 0 0 0-10 10c0 8 10 20 10 20s10-12 10-20A10 10 0 0 0 12 0zm0 14a4 4 0 1 1 0-8 4 4 0 0 1 0 8z"/></svg><span>12/84 Linden Rd, Glen Iris,<br>VIC 3146</span></li>
</ul>
<h3 class="abs f-head" style="left:884px">Request a Call</h3>
<div class="abs f-field" style="top:2402px">Name</div>
<div class="abs f-field" style="top:2443px">Email</div>
<div class="abs f-submit">Submit</div>
<div class="abs f-rule"></div>
<p class="abs copy">© tavoelectrical.com. All Rights Reserved.</p>

</body>
</html>
```